existing Business Card Re design

We are wanting to re design our cards to reflect our new logo , i have attache the current business cards and new logo
i will need a business card that reflects the following information on each card.

card 1:
Harold Dunsby, President
555-382-9164
info@kpqfoamcoat.com

card 2:
Colin Thresher, Outside Sales
Office: 555-382-9164
Cell: 555-617-2048
Sales@kpqfoamcoat.com

Card 3
Louis Varcoe, Branch Manager
Office: 555-382-9164
Cell: 555-493-7752
Louis@kpqfoamcoat.com

Card 4
I will need a Generic card with no name on it just business
555-382-9164
info@kpqfoamcoat.com

Target Market(s)

Homeowners and Contractors

Contact Information for Business Card

We are wanting to re design our cards to reflect our new logo , i have attache the current business cards and new logo. same info on current card

card 1:
Harold Dunsby, President
555-382-9164
info@kpqfoamcoat.com

card 2:
Office: 555-382-9164
Cell: 555-617-2048
Sales@kpqfoamcoat.com

Card 3
Office: 555-382-9164
Cell: 555-493-7752
Louis@kpqfoamcoat.com

Card 4
555-382-9164
info@kpqfoamcoat.com

Requirements
Must have
• same info as current cards with a added business
"sanitizing"

```html
<!DOCTYPE html>
<html lang="en">
<head>
<meta charset="utf-8">
<title>Kepler Foam Coat — Business Cards</title>
<link href="https://fonts.googleapis.com/css2?family=Open+Sans:wght@400;600;800&display=swap" rel="stylesheet">
<style>
  :root{
    --stage:#d4d4d6;
    --back-top:#1f9ad8;
    --back-mid:#1a3f9a;
    --back-bottom:#0e121c;
    --panel-top:#2c3f92;
    --panel-bottom:#2a8dd0;
    --navy:#14286e;
    --white:#ffffff;
    --ink:#0b0b0b;
  }
  *{box-sizing:border-box;margin:0;padding:0}
  html,body{width:1200px;height:3416px;overflow:hidden}
  body{background:var(--stage);font-family:"Open Sans",Arial,sans-serif}
  .set{height:854px;display:flex;flex-direction:column;align-items:center;justify-content:center;gap:40px}
  .card{width:600px;height:343px;border-radius:22px;overflow:hidden;box-shadow:0 10px 24px rgba(0,0,0,.25)}
  .card-back{
    background:linear-gradient(180deg,var(--back-top) 0%,var(--back-mid) 48%,var(--back-bottom) 100%);
    display:flex;flex-direction:column;align-items:center;justify-content:center;color:var(--white);
  }
  .brand{display:flex;align-items:center;gap:14px;font-weight:800;letter-spacing:-.5px}
  .brand-mark{width:22px;height:22px;background:currentColor}
  .card-back .brand{font-size:44px;color:var(--white)}
  .social{margin-top:34px;display:flex;align-items:center;gap:8px;font-size:15px}
  .social-dot{width:16px;height:16px;border-radius:50%;background:var(--white)}
  .card-front{display:flex;background:var(--white)}
  .front-logo{width:48%;display:flex;align-items:center;justify-content:center;border-right:6px solid var(--ink)}
  .front-logo .brand{font-size:26px;color:var(--navy);flex-direction:column;gap:8px;text-align:center;line-height:1.05}
  .front-logo .brand-mark{width:18px;height:18px}
  .info{flex:1;background:linear-gradient(180deg,var(--panel-top),var(--panel-bottom));color:var(--white);padding:34px 30px 0 30px;display:flex;flex-direction:column;justify-content:center;padding-bottom:30px}
  .name{font-size:25px;font-weight:600;line-height:1.1}
  .role{font-size:13px;margin-top:2px}
  .rule{height:1px;background:rgba(255,255,255,.85);margin:12px 0}
  .address{font-size:14px;line-height:1.35}
  .contacts{list-style:none;font-size:14px;line-height:1.55}
  .contacts li{display:flex;align-items:center;gap:8px}
  .contacts svg{width:13px;height:13px;flex:none;fill:var(--white)}
</style>
</head>
<body>

<svg width="0" height="0" style="position:absolute" aria-hidden="true">
  <symbol id="i-phone" viewBox="0 0 16 16"><path d="M2 5c0-2 2-3 6-3s6 1 6 3l-3 1-1-2H6L5 6 2 5zm2 2h8l2 6H2l2-6zm4 1.5a2 2 0 100 4 2 2 0 000-4z"/></symbol>
  <symbol id="i-mobile" viewBox="0 0 16 16"><path d="M4 1h8v14H4V1zm1.5 1.5v9h5v-9h-5zM8 12.3a.9.9 0 100 1.8.9.9 0 000-1.8z"/></symbol>
  <symbol id="i-mail" viewBox="0 0 16 16"><path d="M1 3h14v10H1V3zm1.5 1.5L8 9l5.5-4.5h-11zM2.5 6v5.5h11V6L8 10.5 2.5 6z"/></symbol>
  <symbol id="i-globe" viewBox="0 0 16 16"><path d="M8 1a7 7 0 110 14A7 7 0 018 1zm0 1.5a5.5 5.5 0 100 11 5.5 5.5 0 000-11zM5 5h3l1 2-2 1 1 3-2 1-1-3-1-1 1-3zm5 0l2 1v3l-2 1V5z"/></symbol>
</svg>

<section class="set">
  <div class="card card-back">
    <div class="brand"><span class="brand-mark"></span>Kepler Foam Coat</div>
    <div class="social"><span class="social-dot"></span>keplerfoamcoat</div>
  </div>
  <div class="card card-front">
    <div class="front-logo"><div class="brand"><span class="brand-mark"></span>Kepler<br>Foam Coat</div></div>
    <div class="info">
      <div class="name">Harold Dunsby</div>
      <div class="role">President</div>
      <div class="rule"></div>
      <div class="address">482 Larkin Ave.<br>Suite 5 Dalton, TX 75990</div>
      <div class="rule"></div>
      <ul class="contacts">
        <li><svg><use href="#i-phone"/></svg>555-382-9164</li>
        <li><svg><use href="#i-mail"/></svg>info@kpqfoamcoat.com</li>
        <li><svg><use href="#i-globe"/></svg>keplerfoamcoat.net</li>
      </ul>
    </div>
  </div>
</section>

<section class="set">
  <div class="card card-back">
    <div class="brand"><span class="brand-mark"></span>Kepler Foam Coat</div>
    <div class="social"><span class="social-dot"></span>keplerfoamcoat</div>
  </div>
  <div class="card card-front">
    <div class="front-logo"><div class="brand"><span class="brand-mark"></span>Kepler<br>Foam Coat</div></div>
    <div class="info">
      <div class="name">Colin Thresher</div>
      <div class="role">Outside Sales</div>
      <div class="rule"></div>
      <div class="address">482 Larkin Ave.<br>Suite 5 Dalton, TX 75990</div>
      <div class="rule"></div>
      <ul class="contacts">
        <li><svg><use href="#i-phone"/></svg>555-382-9164</li>
        <li><svg><use href="#i-mobile"/></svg>555-617-2048</li>
        <li><svg><use href="#i-mail"/></svg>Sales@kpqfoamcoat.com</li>
        <li><svg><use href="#i-globe"/></svg>keplerfoamcoat.net</li>
      </ul>
    </div>
  </div>
</section>

<section class="set">
  <div class="card card-front">
    <div class="front-logo"><div class="brand"><span class="brand-mark"></span>Kepler<br>Foam Coat</div></div>
    <div class="info">
      <div class="name">Louis Varcoe</div>
      <div class="role">Branch Manager</div>
      <div class="rule"></div>
      <div class="address">482 Larkin Ave.<br>Suite 5 Dalton, TX 75990</div>
      <div class="rule"></div>
      <ul class="contacts">
        <li><svg><use href="#i-phone"/></svg>555-382-9164</li>
        <li><svg><use href="#i-mobile"/></svg>555-493-7752</li>
        <li><svg><use href="#i-mail"/></svg>Louis@kpqfoamcoat.com</li>
        <li><svg><use href="#i-globe"/></svg>keplerfoamcoat.net</li>
      </ul>
    </div>
  </div>
  <div class="card card-back">
    <div class="brand"><span class="brand-mark"></span>Kepler Foam Coat</div>
    <div class="social"><span class="social-dot"></span>keplerfoamcoat</div>
  </div>
</section>

<section class="set">
  <div class="card card-front">
    <div class="front-logo"><div class="brand"><span class="brand-mark"></span>Kepler<br>Foam Coat</div></div>
    <div class="info">
      <div class="address">482 Larkin Ave.<br>Suite 5 Dalton, TX 75990</div>
      <div class="rule"></div>
      <ul class="contacts">
        <li><svg><use href="#i-phone"/></svg>555-382-9164</li>
        <li><svg><use href="#i-mail"/></svg>info@kpqfoamcoat.com</li>
        <li><svg><use href="#i-globe"/></svg>keplerfoamcoat.net</li>
      </ul>
    </div>
  </div>
  <div class="card card-back">
    <div class="brand"><span class="brand-mark"></span>Kepler Foam Coat</div>
    <div class="social"><span class="social-dot"></span>keplerfoamcoat</div>
  </div>
</section>

</body>
</html>
```